create clean, simple business card template

using the logo created now we need to create a simple, elegant business card design to suit

Industry/Entity Type

Business

Font styles to use
Other font styles liked:
• segoe ui

Requirements
Must have
• Front:
"Name:"
"Title:"
"Mobile:"
"email:"
and the logo

Back:
Logo
Nice to have
• Text in black but other graphics etc to match colours in logo as provided

```html
<!DOCTYPE html>
<html lang="en">
<head>
<meta charset="utf-8">
<title>Harlow Estates – Business Card</title>
<link rel="stylesheet" href="https://fonts.googleapis.com/css2?family=Open+Sans:wght@400;600;700&display=swap">
<style>
  :root {
    --page-bg: #ecebe8;
    --card-bg: #ffffff;
    --gold: #b59a5e;
    --gold-light: #d2bd8a;
    --charcoal: #3d3b38;
    --ink: #111111;
    --muted: #2a2a2a;
  }
  html, body {
    margin: 0;
    padding: 0;
    width: 1200px;
    height: 1000px;
    overflow: hidden;
    background: var(--page-bg);
    font-family: "Open Sans", "Segoe UI", sans-serif;
  }
  .canvas {
    position: relative;
    width: 1200px;
    height: 1000px;
  }
  .card {
    position: absolute;
    width: 660px;
    height: 377px;
    left: 270px;
    background: var(--card-bg);
    border-radius: 4px;
    box-shadow: 0 6px 20px rgba(0,0,0,0.12);
    overflow: hidden;
  }
  .card--back { top: 70px; }
  .card--front { top: 540px; }
  .card__swoosh {
    position: absolute;
    inset: 0;
    width: 100%;
    height: 100%;
  }

  /* Logo stand-in */
  .brand {
    position: absolute;
    display: flex;
    align-items: center;
    gap: 14px;
  }
  .brand__dot {
    width: 46px;
    height: 46px;
    border-radius: 50%;
    background: var(--charcoal);
  }
  .brand__name {
    font-weight: 600;
    color: var(--gold);
    letter-spacing: 0.06em;
    font-size: 34px;
    line-height: 1;
    white-space: nowrap;
  }
  .card--back .brand {
    left: 50%;
    top: 150px;
    transform: translateX(-50%);
  }
  .card--front .brand {
    right: 48px;
    top: 64px;
  }
  .card--front .brand__name { font-size: 30px; }
  .brand__divider {
    width: 1px;
    height: 74px;
    background: var(--charcoal);
    margin: 0 4px;
  }

  /* Front details */
  .person {
    position: absolute;
    left: 60px;
    top: 190px;
  }
  .person__name {
    margin: 0;
    font-size: 30px;
    font-weight: 700;
    color: var(--ink);
    line-height: 1.1;
  }
  .person__title {
    margin: 2px 0 0;
    font-size: 16px;
    font-weight: 400;
    color: var(--muted);
  }
  .details-rule {
    position: absolute;
    left: 300px;
    top: 205px;
    width: 1px;
    height: 60px;
    background: var(--ink);
  }
  .contact {
    position: absolute;
    right: 40px;
    bottom: 48px;
    margin: 0;
    padding: 0;
    list-style: none;
    text-align: right;
  }
  .contact__item {
    display: flex;
    justify-content: flex-end;
    align-items: center;
    gap: 8px;
    font-size: 17px;
    color: var(--ink);
    line-height: 1.6;
  }
  .contact__sep { font-weight: 700; }
  .contact__icon {
    width: 18px;
    height: 18px;
    fill: var(--gold);
  }
</style>
</head>
<body>
<main class="canvas">

  <section class="card card--back" aria-label="Card back">
    <svg class="card__swoosh" viewBox="0 0 660 377" aria-hidden="true">
      <path d="M0 300 C 150 330, 300 360, 420 377 L0 377 Z" fill="var(--gold-light)"/>
      <path d="M0 300 C 150 330, 300 360, 420 377" fill="none" stroke="var(--gold)" stroke-width="4"/>
    </svg>
    <div class="brand">
      <span class="brand__dot"></span>
      <span class="brand__name">HARLOW ESTATES</span>
    </div>
  </section>

  <section class="card card--front" aria-label="Card front">
    <svg class="card__swoosh" viewBox="0 0 660 377" aria-hidden="true">
      <path d="M0 240 C 120 300, 320 345, 660 355 L660 377 L0 377 Z" fill="var(--gold)"/>
      <path d="M0 250 C 130 310, 330 352, 660 360 L660 377 L0 377 Z" fill="#ffffff"/>
      <path d="M0 262 C 140 322, 340 360, 660 366 L660 377 L0 377 Z" fill="var(--gold-light)"/>
      <path d="M0 220 C 120 285, 330 335, 660 350" fill="none" stroke="var(--charcoal)" stroke-width="6"/>
    </svg>

    <div class="brand">
      <span class="brand__dot"></span>
      <span class="brand__divider"></span>
      <span class="brand__name">HARLOW ESTATES</span>
    </div>

    <div class="person">
      <h1 class="person__name">Daniel Reeve</h1>
      <p class="person__title">Property Manager</p>
    </div>
    <span class="details-rule"></span>

    <ul class="contact">
      <li class="contact__item">
        <span>+ 000 - 1234 - 5678</span><span class="contact__sep">:</span>
        <svg class="contact__icon" viewBox="0 0 24 24" aria-label="Phone"><path d="M6.6 10.8a15.1 15.1 0 0 0 6.6 6.6l2.2-2.2a1 1 0 0 1 1-.25 11.4 11.4 0 0 0 3.6.57 1 1 0 0 1 1 1V20a1 1 0 0 1-1 1A17 17 0 0 1 3 4a1 1 0 0 1 1-1h3.5a1 1 0 0 1 1 1c0 1.25.2 2.45.57 3.57a1 1 0 0 1-.25 1z"/></svg>
      </li>
      <li class="contact__item">
        <span>daniel@harlowestates.com</span><span class="contact__sep">:</span>
        <svg class="contact__icon" viewBox="0 0 24 24" aria-label="Email"><path d="M2 5h20v14H2z M2 5l10 8 10-8" fill="var(--gold)" stroke="#fff" stroke-width="1.4"/></svg>
      </li>
    </ul>
  </section>

</main>
</body>
</html>
```